Exhibition Stand Design for innovative Social Business

We are an innovative social business empowering people to value nature through KEV, a complementary digital currency. We have attached the MY_KEV branding document, and are needing a design for our exhibition stand (https://salonvorta.example/produit/stand-parapluie-classic-pvc-3x4c/. The attached doc mocks up a stand on page 32, though we would like some messaging included, in line with our website www.mykev.example. You will see there how the branding concept has been implemented with the OUR:ROOTS, COINS, EARTH wording, as well as All gain together. Our green colours are included in the branding document. Many thanks!

Industry/Entity Type

Environment

Font styles to use
Other font styles liked:
• As per our attached fonts

Requirements
Must have
• Our attached branding guidelines gives our look and feel - Innovative / Dynamic / Vibrant / Reliable / Accessible / Connected.

```html
<!DOCTYPE html>
<html lang="en">
<head>
<meta charset="utf-8">
<title>KEV Exhibition Stand</title>
<link rel="stylesheet" href="https://fonts.googleapis.com/css2?family=Outfit:wght@500;600&display=swap">
<style>
  :root {
    --page-bg: #e9e9e9;
    --band-white: #ffffff;
    --ink: #111111;
    --brand-green: #2ee05a;
    --hill-dark: #2f7a32;
    --hill-mid: #4f9a3f;
    --hill-light: #7cbf63;
    --sky: #a9dcb4;
    --box-tint: rgba(38, 58, 40, 0.45);
    --type-white: #ffffff;
  }
  * { margin: 0; padding: 0; box-sizing: border-box; }
  html, body {
    width: 1200px;
    height: 1000px;
    overflow: hidden;
    background: var(--page-bg);
    font-family: "Outfit", sans-serif;
  }
  .stand-graphic {
    position: absolute;
    left: 100px;
    top: 110px;
    width: 1000px;
    height: 720px;
    background: var(--band-white);
    overflow: hidden;
  }
  .header-band {
    position: absolute;
    left: 0; top: 0;
    width: 100%;
    height: 140px;
    background: var(--band-white);
    border-bottom: 5px solid var(--ink);
    display: flex;
    align-items: center;
    justify-content: space-between;
    padding: 0 52px 0 58px;
  }
  .brand-name {
    display: flex;
    align-items: center;
    gap: 18px;
    font-weight: 600;
    font-size: 72px;
    color: var(--ink);
    line-height: 1;
  }
  .brand-dot {
    width: 28px;
    height: 28px;
    border-radius: 50%;
    background: var(--brand-green);
  }
  .tagline {
    font-weight: 600;
    font-size: 48px;
    color: var(--ink);
    padding-top: 24px;
    line-height: 1;
  }
  .landscape {
    position: absolute;
    left: 0; top: 145px;
    width: 100%;
    height: 575px;
    background:
      linear-gradient(180deg, var(--sky) 0%, #93c996 22%, var(--hill-light) 32%, var(--hill-mid) 55%, var(--hill-dark) 80%, #3f8a36 100%);
  }
  .message-box {
    position: absolute;
    left: 93px;
    top: 223px;
    width: 352px;
    height: 357px;
    border-radius: 16px;
    background: var(--box-tint);
    padding: 10px 0 0 36px;
  }
  .message-box p {
    font-weight: 500;
    font-size: 64px;
    line-height: 78px;
    color: var(--type-white);
  }
  .message-box .lead {
    color: var(--brand-green);
  }
</style>
</head>
<body>
  <main class="stand-graphic">
    <header class="header-band">
      <span class="brand-name"><span class="brand-dot"></span>KEV</span>
      <span class="tagline">all gain together</span>
    </header>
    <div class="landscape" role="img" aria-label="Photograph of rolling green grassy hills under a pale sky"></div>
    <section class="message-box">
      <p class="lead">OUR:</p>
      <p>ROOTS</p>
      <p>COINS</p>
      <p>EARTH</p>
    </section>
  </main>
</body>
</html>
```